WP website design (N Kentucky)

We need a wordpress design that will incorporate a professional color scheme with company logo in a clean layout. The design needs to consider that this will be developed on a responsive theme. Colors are undetermined - can use a dark red - logo is black so creative use of colors will be important. Client wants a 'modern' look.
Updates

Project Deadline Extended
Reason: Client wants a few more designs

Industry/Entity Type

It Company

Font styles to use
Serif
Sans Serif

Requirements
Must have
• Must Have:
- Navigation: 1) Home 2) Auctions 3) Auction Marketing 4) Buying at Auction 5) About Us 6) Contact Us

Site will have a slideshow element and the following widgets: 1) Featured Auctions 2) Testimonials blog widget 3) 'Auction Alerts' email sign up 4) Fz Chirpa Zelnix+ icons. Colors can be the meadowline7 gold/black from http://www.brambleridgehouses.example/

In the footer, there will be smaller company logo, the affiliations logo, and contact info below:
Copperfield Gavel Sales, LLC / Wes Pellham
email: wespell@mailbox.example; wes.pellham@ml7.example
phone: (859) 555-0147 mobile phone: (859)555-0182
Domain: http://www.copperfieldgavelsales.example/
Nice to have
• - - Site will have drop-down menus - please indicate the styling, for instance the dropdown menus 1) Upcoming Auctions 2) Past Auctions under the 'Auctions' link

```html
<!DOCTYPE html>
<html lang="en">
<head>
<meta charset="utf-8">
<title>Copperfield Gavel Sales, LLC</title>
<link href="https://fonts.googleapis.com/css2?family=Questrial&family=Arimo:wght@400;700&display=swap" rel="stylesheet">
<style>
:root{
  --red:#c4000b;
  --red-dark:#8e0008;
  --ink:#111;
  --dark:#2b2b2b;
  --panel:#3a3a3a;
  --footer:#232323;
  --light:#dcdcdc;
  --text:#333;
  --muted:#666;
  --white:#fff;
}
*{box-sizing:border-box;margin:0;padding:0}
html,body{width:711px;height:1200px;overflow:hidden;background:#000}
body{position:relative;font-family:"Arimo",Arial,sans-serif;color:var(--text)}
.abs{position:absolute}
.display{font-family:"Questrial",sans-serif}
.accent{color:var(--red)}

/* header */
.site-header{left:0;top:0;width:711px;height:55px;background:linear-gradient(#1a1d24,#0c0e12);border-bottom:1px solid var(--red-dark)}
.brand{left:84px;top:0;width:143px;height:55px;background:#f1f1f1;display:flex;align-items:center;gap:6px;padding:0 8px}
.brand-mark{width:14px;height:14px;background:var(--ink);flex:none}
.brand-name{font-family:"Questrial",sans-serif;font-size:10px;line-height:11px;color:var(--ink);text-transform:uppercase}
.main-nav{left:256px;top:0;height:55px;display:flex}
.main-nav a{font-family:"Questrial",sans-serif;font-size:7.5px;color:var(--white);text-decoration:none;text-transform:uppercase;height:55px;display:flex;align-items:center;padding:0 9px}
.main-nav a.current{background:var(--red);padding:0 9px}
.search{left:532px;top:4px;width:94px;height:11px;background:#e6e6e6;border-radius:2px;font-size:7px;color:#999;padding-left:4px;line-height:11px}

/* hero */
.hero{left:0;top:55px;width:711px;height:327px;background:linear-gradient(180deg,#1d3550 0%,#12233a 30%,#1b1a22 60%,#0b0b0e 100%)}
.hero-arrow{width:34px;height:34px;border-radius:50%;background:rgba(0,0,0,.45);top:199px}
.hero-caption{left:316px;top:281px;color:var(--white);text-align:left}
.hero-caption .line1{font-family:"Questrial",sans-serif;font-size:12.5px;letter-spacing:.3px;text-transform:uppercase}
.hero-caption .line2{font-family:"Questrial",sans-serif;font-size:10px;margin-top:7px;text-transform:uppercase}
.hero-dots{left:91px;top:342px;display:flex;gap:5px}
.hero-dots span{width:7px;height:7px;border-radius:50%;background:#777}
.hero-dots span:first-child{background:#ddd}

/* category bar */
.category-bar{left:84px;top:356px;width:544px;height:59px;background:var(--panel);box-shadow:0 6px 8px rgba(0,0,0,.35);display:flex;gap:28px;padding:16px 16px 0}
.category{width:155px;height:32px;background:#1f1f1f;display:flex;align-items:center;border-right:2px solid #555}
.category-icon{width:36px;height:32px;background:var(--red);display:flex;align-items:center;justify-content:center;flex:none}
.category-label{color:var(--white);font-family:"Questrial",sans-serif;padding-left:8px;line-height:12px}

/* welcome */
.intro{left:0;top:382px;width:711px;height:198px;background:var(--light)}
.section-title{font-family:"Arimo",sans-serif;font-size:11px;color:var(--ink)}
.intro-copy{font-size:6.5px;line-height:11px;color:var(--text)}
.read-more{font-size:7px;color:var(--red);text-transform:uppercase;text-decoration:none}
.badge{width:42px;height:28px;background:#1b1b1b;border-radius:3px}
.badge.round{border-radius:50%;width:58px}

/* widgets band */
.widgets{left:0;top:580px;width:711px;height:180px;background:#000}
.widget{top:40px;width:171px;height:125px;background:var(--panel);text-align:center}
.widget-icon{top:-24px;left:66px;width:42px;height:39px;background:var(--red);display:flex;align-items:center;justify-content:center}
.widget-title{font-family:"Questrial",sans-serif;font-size:12px;color:var(--white);margin-top:30px}
.widget-copy{font-size:6.2px;line-height:11px;color:#eee;text-align:left;padding:10px 7px 0}
.widget-btn{display:inline-block;margin-top:6px;background:var(--white);color:var(--red);font-size:6.5px;padding:5px 7px;text-transform:uppercase}

/* news / testimonials */
.news{left:0;top:760px;width:711px;height:200px;background:var(--light)}
.news-title{font-size:12px;color:var(--ink)}
.rule{height:1px;background:#bbb}
.date{width:34px;height:30px;border:1px solid #bbb;background:var(--white);text-align:center}
.date .m{background:var(--red);color:var(--white);font-size:9px;font-weight:700;height:14px;line-height:14px}
.date .d{font-size:10px;font-weight:700;color:#333;line-height:15px}
.news-head{font-size:7px;color:var(--red)}
.news-copy{font-size:6.3px;line-height:11px;color:var(--text)}
.avatar{width:35px;height:35px;border-radius:50%;background:var(--white);border:3px solid #c9c9c9}
.quote-mark{font-size:10px;color:#999;font-family:Georgia,serif}

/* featured auctions */
.featured{left:0;top:960px;width:711px;height:109px;background:var(--light);border-top:1px solid #bbb}
.featured-tab{left:283px;top:-1px;width:146px;height:21px;background:var(--red);border-radius:0 0 14px 14px;color:var(--white);font-family:"Questrial",sans-serif;font-size:12.5px;text-align:center;line-height:20px}
.thumb{top:29px;width:151px;height:72px;border:3px solid #ccc;box-shadow:0 3px 5px rgba(0,0,0,.3)}
.thumb.active{border-color:var(--red)}
.thumb-photo{width:100%;height:100%;background:linear-gradient(180deg,#7ca2c3 0%,#4c6f8f 55%,#2e3a45 100%)}
.red-line{left:0;top:1069px;width:711px;height:2px;background:var(--red)}

/* footer */
.site-footer{left:0;top:1071px;width:711px;height:109px;background:var(--footer)}
.footer-nav{left:86px;top:34px;list-style:none}
.footer-nav li{font-size:6.5px;color:var(--white);line-height:13.5px}
.footer-nav li::before{content:"›";margin-right:6px}
.contact-title{left:188px;top:14px;font-family:"Questrial",sans-serif;font-size:10px;color:var(--white)}
.contact-row{left:186px;display:flex;gap:9px;color:var(--white);font-size:6.5px;line-height:10px}
.contact-row b{font-weight:700}
.footer-brand{left:513px;top:10px;width:108px;height:41px;background:#555;display:flex;align-items:center;gap:5px;padding:0 7px}
.footer-brand .brand-name{color:#222;font-size:8.5px;line-height:9.5px}
.footer-badge{top:70px;height:20px;background:#ddd;border-radius:2px}
.bottom-bar{left:0;top:1180px;width:711px;height:20px;background:#000;border-top:1px solid #333}
</style>
</head>
<body>

<header class="site-header abs">
  <div class="brand abs">
    <span class="brand-mark"></span>
    <span class="brand-name">Copperfield Gavel Sales, LLC</span>
  </div>
  <nav class="main-nav abs">
    <a class="current" href="#">Home</a>
    <a href="#">Auctions</a>
    <a href="#">Auction Marketing</a>
    <a href="#">Buying at Auction</a>
    <a href="#">About Us</a>
    <a href="#">Contact Us</a>
  </nav>
  <div class="search abs">Search</div>
</header>

<section class="hero abs" role="img" aria-label="Slideshow photo: city skyline of lit high-rise towers at night above a harbour">
  <div class="hero-arrow abs" style="left:87px">
    <svg width="34" height="34" viewBox="0 0 34 34"><path d="M20 10 L13 17 L20 24" stroke="#fff" stroke-width="3" fill="none"/></svg>
  </div>
  <div class="hero-arrow abs" style="left:595px">
    <svg width="34" height="34" viewBox="0 0 34 34"><path d="M14 10 L21 17 L14 24" stroke="#fff" stroke-width="3" fill="none"/></svg>
  </div>
  <div class="hero-caption abs">
    <div class="line1">Superbly located, invitingly ready to enjoy</div>
    <div class="line2"><span class="accent">Feature auction:</span> 42 Harrowgate Lane, Fenwick KY 41099</div>
  </div>
  <div class="hero-dots abs"><span></span><span></span><span></span></div>
</section>

<section class="intro abs">
  <div class="abs" style="left:85px;top:56px;width:352px">
    <h1 class="section-title">Welcome to <span class="accent">Copperfield Gavel Sales, LLC</span></h1>
    <p class="intro-copy" style="margin-top:8px">Lorem ipsum dolor sit amet, consectetur adipiscing elit. Proin pulvinar eros in imperdiet porttitor. Praesent velit justo, placerat ut ornare aliquet, venenatis vel justo. Nulla porttitor enim vitae nibh scelerisque, nec laoreet libero posuere. Integer ut neque ut purus dictum auctor. Cras tincidunt odio a pharetra iaculis. Nam in arcu eu tortor consequat tempor. Vivamus eu convallis risus.</p>
    <p class="intro-copy" style="margin-top:9px">Mauris pulvinar, eros ac elementum tempus,</p>
    <a class="read-more" href="#" style="display:block;margin-top:12px">Read more</a>
  </div>
  <div class="abs" style="left:456px;top:56px;width:180px">
    <h2 class="section-title" style="font-size:9.5px">Our <span class="accent">Affiliations</span></h2>
    <div style="display:flex;gap:10px;margin-top:12px;align-items:center">
      <div class="badge" style="width:30px" role="img" aria-label="Partner badge"></div>
      <div class="badge" style="width:56px" role="img" aria-label="Certification badge"></div>
      <div class="badge round" role="img" aria-label="Association badge"></div>
    </div>
    <p class="intro-copy" style="margin-top:18px;color:var(--muted);line-height:8.5px">Lorem ipsum dolor sit amet, consectetur adipiscing elit. Proin pulvinar eros in imperdiet porttitor. Praesent velit justo, placerat ut ornare aliquet, venenatis vel justo.</p>
    <a class="read-more" href="#" style="display:block;margin-top:8px">Read more</a>
  </div>
</section>

<div class="category-bar abs">
  <div class="category">
    <span class="category-icon"><svg width="18" height="18" viewBox="0 0 18 18" fill="#fff"><rect x="2" y="6" width="6" height="11"/><rect x="9" y="2" width="7" height="15"/></svg></span>
    <span class="category-label" style="font-size:12.5px">High Rises</span>
  </div>
  <div class="category">
    <span class="category-icon"><svg width="18" height="18" viewBox="0 0 18 18" fill="#fff"><path d="M1 6 L9 1 L17 6 Z"/><rect x="3" y="7" width="2" height="7"/><rect x="8" y="7" width="2" height="7"/><rect x="13" y="7" width="2" height="7"/><rect x="1" y="15" width="16" height="2"/></svg></span>
    <span class="category-label" style="font-size:10px">Government Office<br>Buildings</span>
  </div>
  <div class="category">
    <span class="category-icon"><svg width="20" height="18" viewBox="0 0 20 18" fill="none" stroke="#fff" stroke-width="1.3"><path d="M2 17 V7 L10 2 L18 7 V17 Z"/><path d="M5 9h3v3H5zM12 9h3v3h-3zM5 13h3v3H5zM12 13h3v3h-3z"/></svg></span>
    <span class="category-label" style="font-size:10px">Apartment<br>Communities</span>
  </div>
</div>

<section class="widgets abs">
  <article class="widget abs" style="left:89px">
    <div class="widget-icon abs"><svg width="22" height="22" viewBox="0 0 22 22" fill="none" stroke="#fff" stroke-width="1.5"><path d="M3 20V8l6-3v15M9 20V3l9 4v13M2 20h18"/></svg></div>
    <h3 class="widget-title">Featured <span class="accent">Auctions</span></h3>
    <p class="widget-copy">Lorem ipsum dolor sit amet, consectetur adipiscing elit. Proin pulvinar eros in imperdiet porttitor. Praesent velit justo, placerat ut ornare aliquet, venenatis vel justo. Nulla porttitor enim vitae nibh scelerisque, nec laoreet libero</p>
    <span class="widget-btn">Read more</span>
  </article>
  <article class="widget abs" style="left:273px">
    <div class="widget-icon abs"><svg width="22" height="22" viewBox="0 0 22 22" fill="none" stroke="#fff" stroke-width="1.5"><rect x="2" y="2" width="8" height="8" rx="1"/><circle cx="15" cy="15" r="5"/><path d="M14 4h5v5M8 20H3v-5"/></svg></div>
    <h3 class="widget-title">Client <span class="accent">Testimonials</span></h3>
    <p class="widget-copy">Lorem ipsum dolor sit amet, consectetur adipiscing elit. Proin pulvinar eros in imperdiet porttitor. Praesent velit justo, placerat ut ornare aliquet, venenatis vel justo. Nulla porttitor enim vitae nibh scelerisque, nec laoreet libero</p>
    <span class="widget-btn">Read more</span>
  </article>
  <article class="widget abs" style="left:457px">
    <div class="widget-icon abs"><svg width="22" height="22" viewBox="0 0 22 22" fill="none" stroke="#fff" stroke-width="1.5"><path d="M4 11 L11 4 L18 11M6 9v5h10V9"/><path d="M2 17c4 0 6 2 9 2s6-2 9-4"/></svg></div>
    <h3 class="widget-title">Auction <span class="accent">Alerts</span></h3>
    <p class="widget-copy">Lorem ipsum dolor sit amet, consectetur adipiscing elit. Proin pulvinar eros in imperdiet porttitor. Praesent velit justo, placerat ut ornare aliquet, venenatis vel justo. Nulla porttitor enim vitae nibh scelerisque, nec laoreet libero</p>
    <span class="widget-btn">Read more</span>
  </article>
</section>

<section class="news abs">
  <div class="abs" style="left:84px;top:16px;width:262px">
    <h2 class="news-title">Latest <span class="accent">News</span></h2>
    <div class="rule" style="margin-top:6px"></div>
  </div>
  <div class="abs" style="left:85px;top:45px;width:262px;display:flex;gap:9px">
    <div class="date"><div class="m">JAN</div><div class="d">18</div></div>
    <div style="width:218px">
      <div class="news-head">Ut wisi enim ad min ve nostrud exerci ta ull amcorper</div>
      <div class="rule" style="margin:3px 0 2px;background:#ccc"></div>
      <p class="news-copy">Lorem ipsum dolor sit amet, consectetur adipiscing elit. Proin pulvinar eros in imperdiet porttitor. Praesent velit justo, placerat ut ornare aliquet, venenatis vel justo. Nulla porttitor enim vitae</p>
    </div>
  </div>
  <div class="abs" style="left:85px;top:111px;width:262px;display:flex;gap:9px">
    <div class="date"><div class="m">JAN</div><div class="d">18</div></div>
    <div style="width:218px">
      <div class="news-head">Ut wisi enim ad min ve nostrud exerci ta ull amcorper</div>
      <div class="rule" style="margin:3px 0 2px;background:#ccc"></div>
      <p class="news-copy">Lorem ipsum dolor sit amet, consectetur adipiscing elit. Proin pulvinar eros in imperdiet porttitor. Praesent velit justo, placerat ut ornare aliquet, venenatis vel justo. Nulla porttitor enim vitae</p>
    </div>
  </div>
  <a class="read-more abs" href="#" style="left:89px;top:161px">Read more</a>
  <div class="abs" style="left:355px;top:25px;width:1px;height:160px;background:#aaa"></div>

  <div class="abs" style="left:362px;top:16px;width:263px">
    <h2 class="news-title">Clients <span class="accent">Testimonials</span></h2>
    <div class="rule" style="margin-top:6px"></div>
  </div>
  <div class="abs" style="left:365px;top:45px;width:125px">
    <div style="display:flex;gap:8px">
      <div class="avatar"></div>
      <div style="padding-top:5px"><div class="news-head" style="font-size:6.5px">Lorem lipsum</div><div class="news-copy" style="margin-top:2px">Mr Clients Name</div></div>
    </div>
    <p class="news-copy" style="margin-top:3px"><span class="quote-mark">“</span> Lorem ipsum dolor sit amet, consectetur adipiscing elit. Proin pulvinar eros in imperdiet porttitoscelerisque, nec laoreet libero posuere. Integer ut neque ut <span class="quote-mark">”</span></p>
  </div>
  <div class="abs" style="left:502px;top:45px;width:125px">
    <div style="display:flex;gap:8px">
      <div class="avatar"></div>
      <div style="padding-top:5px"><div class="news-head" style="font-size:6.5px">Lorem lipsum</div><div class="news-copy" style="margin-top:2px">Mr Clients Name</div></div>
    </div>
    <p class="news-copy" style="margin-top:3px"><span class="quote-mark">“</span> Lorem ipsum dolor sit amet, consectetur adipiscing elit. Proin pulvinar eros in imperdiet porttitoscelerisque, nec laoreet libero posuere. Integer ut neque . <span class="quote-mark">”</span></p>
  </div>
  <a class="read-more abs" href="#" style="left:369px;top:161px">Read more</a>
</section>

<section class="featured abs">
  <div class="featured-tab abs">Featured Auctions</div>
  <svg class="abs" style="left:82px;top:55px" width="12" height="14" viewBox="0 0 12 14"><path d="M9 2 L3 7 L9 12" stroke="#555" stroke-width="2.5" fill="none"/></svg>
  <div class="thumb active abs" style="left:102px"><div class="thumb-photo" role="img" aria-label="Auction property: modern glass office building"></div></div>
  <svg class="abs" style="left:262px;top:55px" width="12" height="14" viewBox="0 0 12 14"><path d="M3 2 L9 7 L3 12" stroke="#555" stroke-width="2.5" fill="none"/></svg>
  <div class="thumb abs" style="left:282px"><div class="thumb-photo" role="img" aria-label="Auction property: cluster of office towers"></div></div>
  <div class="thumb abs" style="left:460px"><div class="thumb-photo" style="background:linear-gradient(180deg,#3f6a9c 0%,#2c4c74 60%,#1d2a3a 100%)" role="img" aria-label="Auction property: high-rise towers at dusk"></div></div>
  <svg class="abs" style="left:617px;top:55px" width="12" height="14" viewBox="0 0 12 14"><path d="M3 2 L9 7 L3 12" stroke="#555" stroke-width="2.5" fill="none"/></svg>
</section>

<div class="red-line abs"></div>

<footer class="site-footer abs">
  <ul class="footer-nav abs">
    <li>Home</li><li>Company</li><li>Development</li><li>Staff</li><li>Contact</li>
  </ul>
  <div class="abs" style="left:170px;top:28px;width:1px;height:70px;background:#444"></div>
  <h3 class="contact-title abs">Contact Information</h3>
  <div class="contact-row abs" style="top:35px">
    <svg width="8" height="10" viewBox="0 0 8 10"><path d="M4 0a3.5 3.5 0 0 0-3.5 3.5C.5 6 4 10 4 10s3.5-4 3.5-6.5A3.5 3.5 0 0 0 4 0z" fill="#c4000b"/><circle cx="4" cy="3.5" r="1.2" fill="#232323"/></svg>
    <span>Copperfield Gavel Sales, LLC</span>
  </div>
  <div class="contact-row abs" style="top:53px">
    <svg width="9" height="7" viewBox="0 0 9 7" style="margin-top:2px"><rect width="9" height="7" fill="#c4000b"/><path d="M0 0 L4.5 4 L9 0" stroke="#232323" fill="none"/></svg>
    <span><b>wespell@mailbox.example</b><br><b>wes.pellham@ml7.example</b></span>
  </div>
  <div class="contact-row abs" style="top:79px">
    <svg width="9" height="9" viewBox="0 0 9 9" style="margin-top:2px"><path d="M2 0 L4 2.5 L3 3.8 Q4.5 6 5.2 6 L6.5 5 L9 7 L7.5 9 Q3 8.5 0 2 Z" fill="#c4000b"/></svg>
    <span><b>(859) 555-0147</b><br><b>(859) 555-0182</b></span>
  </div>
  <div class="footer-brand abs">
    <span class="brand-mark" style="width:11px;height:11px;background:#222"></span>
    <span class="brand-name">Copperfield Gavel Sales, LLC</span>
  </div>
  <div class="footer-badge abs" style="left:513px;width:18px" role="img" aria-label="Partner badge"></div>
  <div class="footer-badge abs" style="left:537px;width:36px" role="img" aria-label="Certification badge"></div>
  <div class="footer-badge abs" style="left:583px;width:40px;border-radius:50%" role="img" aria-label="Association badge"></div>
</footer>

<div class="bottom-bar abs"></div>

</body>
</html>
```